Bold Cover needed for a book on Workplace Bullying

I need a book cover design for a book titled, “Iron Silence?” The book recounts my story of bullying in the workplace. It also includes chapters on how readers can minimize/stop workplace bullying, write an effective complaint, and ensure their own mental wellbeing.
I am looking for a bold design using red and black, and possibly distressed lettering. The covers of other books dealing with this subject do not reflect my vision. They are often too childish or look too academic. This book needs to stress the serious nature of a toxic workplace, while appealing to readers experiencing a similar situation. I’d like the cover to reflect the mental anguish associated with workplace bullying (hence the distressed lettering).
I have included a cover that appeals to me (although the coloring is wrong). That said, I am also very happy (and excited) to see your creative input!
On the cover, it should have the following:
Title: Iron Silence?
Subtitle: How the Harbour Works Department Condones Bullying & Ruins Lives
Author: Owen Frick
Other relevant details:
Book size: 5.5” x 8.5”
Back cover will have a blurb, author picture/short bio, and barcode
The blurb on the back cover reads:
Undermining, intimidation and threats
Despite the Department of Harbour Works allegedly holding a zero tolerance for bullying, these behaviours were an everyday occurrence in at least one workplace. Even after a decade of complaints, numerous witnesses and physical proof, the department failed to act. Instead, they looked the other way, allowing one powerful and well-connected individual to end careers and ruin lives.
After being targeted, one teacher resolved to put an end to the abuse experienced by more than fifty employees. His startling story reveals the relentless bullying, mental health ramifications, and insidious tactics used to cover up the corrosive behaviour.
Those who have experienced a toxic workplace will also find much needed support and guidance, intended to minimise suffering and detail a clear way forward. Chapters include dealing with bullying in the workplace, how to lodge a successful complaint, and how to stay sane during any potential legal action.

```html
<!DOCTYPE html>
<html lang="en">
<head>
<meta charset="utf-8">
<title>Iron Silence? — Book Cover</title>
<link rel="stylesheet" href="https://fonts.googleapis.com/css2?family=Bebas+Neue&family=Montserrat:wght@500&display=swap">
<style>
  :root {
    --backdrop: #e8e8e8;
    --cover-black: #1a1a1a;
    --cover-red: #e41b23;
    --type-white: #ffffff;
  }
  html, body {
    margin: 0;
    padding: 0;
    width: 1200px;
    height: 2400px;
    overflow: hidden;
    background: var(--backdrop);
  }
  .canvas {
    position: relative;
    width: 1200px;
    height: 2400px;
  }
  .book-cover {
    position: absolute;
    left: 100px;
    top: 427px;
    width: 1000px;
    height: 1545px;
    background: radial-gradient(ellipse at 50% 45%, #222 0%, var(--cover-black) 60%, #141414 100%);
    overflow: hidden;
  }
  .subtitle {
    position: absolute;
    top: 58px;
    left: 0;
    right: 0;
    margin: 0;
    text-align: center;
    font-family: "Montserrat", sans-serif;
    font-weight: 500;
    font-size: 31px;
    line-height: 57px;
    letter-spacing: 0.13em;
    color: var(--type-white);
    text-transform: uppercase;
  }
  .title-lead {
    position: absolute;
    top: 255px;
    left: 0;
    right: 0;
    height: 825px;
    display: flex;
    align-items: center;
    justify-content: center;
    margin: 0;
    font-family: "Bebas Neue", sans-serif;
    font-weight: 400;
    font-size: 470px;
    line-height: 1;
    color: var(--cover-red);
    letter-spacing: 0.02em;
  }
  .title-lead span {
    display: inline-block;
    transform: scaleY(1.6);
    padding-top: 0.08em;
  }
  .title-main {
    position: absolute;
    top: 1125px;
    left: 0;
    right: 0;
    margin: 0;
    text-align: center;
    font-family: "Bebas Neue", sans-serif;
    font-weight: 400;
    font-size: 232px;
    line-height: 1;
    letter-spacing: 0.01em;
    color: var(--type-white);
  }
  .author {
    position: absolute;
    top: 1390px;
    left: 0;
    right: 0;
    margin: 0;
    text-align: center;
    font-family: "Montserrat", sans-serif;
    font-weight: 500;
    font-size: 54px;
    line-height: 1;
    letter-spacing: 0.26em;
    color: var(--type-white);
    text-transform: uppercase;
  }
</style>
</head>
<body>
  <main class="canvas">
    <section class="book-cover" aria-label="Front cover of Iron Silence? by Owen Frick">
      <p class="subtitle">How the Harbour Works Department<br>Condones Bullying &amp; Ruins Lives</p>
      <h1 class="title-lead"><span>IRON</span></h1>
      <p class="title-main">SILENCE?</p>
      <p class="author">Owen Frick</p>
    </section>
  </main>
</body>
</html>
```